Flyer: Steady Steps, Bright Days

Please create a two (2) page flyer. We welcome minor updates/ changes to the Steady Steps Bright Days flyer that is attached as a word document. We are aiming for the same general look and feel as the original PDF attached (please note that we have updated the content and would like the designers to use what is listed in the word document).
We encourage you to provide multiple versions using pictures of different people we have on hand. Our team currently likes how the lady in the picture is looking in the direction of the text - we encourage designers to please flip the photo if needed to make this possible. We also give the permission to crop the photos as needed to fit the design better aesthetically. In addition, the team wondered about having a pdf file that allows the user to easily change out the graphic between different photos to reflect different communities best—not sure if that is as easy as it sounds. Please remember to include the funding statement - you can find it within both of the current documents. For more information about our project, please visit https://novelmarrow.org/wellness-path/

```html
<!DOCTYPE html>
<html lang="en">
<head>
<meta charset="utf-8">
<title>Steady Steps, Bright Days – Flyer</title>
<link href="https://fonts.googleapis.com/css2?family=Poppins:ital,wght@0,400;0,500;0,600;0,700;1,700;1,800&display=swap" rel="stylesheet">
<style>
  :root{
    --teal:#3a9ea5;
    --red:#b5534f;
    --maroon:#8b3a33;
    --deep:#6b2620;
    --pink:#fbe3e1;
    --ink:#333333;
    --brown:#5a2418;
    --paper:#ffffff;
    --backdrop:#eceef1;
  }
  *{box-sizing:border-box;margin:0;padding:0}
  html,body{width:1200px;height:3747px;overflow:hidden}
  body{
    background:var(--backdrop);
    font-family:"Poppins",sans-serif;color:var(--ink);
    display:flex;flex-direction:column;align-items:center;justify-content:space-evenly;
  }
  .page{position:relative;width:1140px;height:1475px;background:var(--paper);box-shadow:0 6px 18px rgba(0,0,0,.18);overflow:hidden}
  .abs{position:absolute}

  /* page one */
  .title{left:59px;top:44px;font-weight:600;font-size:50px;line-height:1.08;letter-spacing:-.5px;color:#3d3d3d;text-transform:uppercase}
  .title .accent{color:var(--red);font-weight:700;display:block}
  .banner{background:var(--teal);color:#fff;text-transform:uppercase;font-weight:500;font-size:27px;line-height:1.3;letter-spacing:.5px}
  .banner--side{left:548px;right:0;top:59px;height:90px;padding:12px 0 0 28px}
  .intro{left:59px;top:178px;width:452px;font-size:16px;line-height:1.3}
  .stat-pill{left:55px;height:44px;width:158px;border-radius:22px;background:var(--teal);border:3px solid #bfe3e5;color:#fff;font-style:italic;font-weight:800;font-size:34px;line-height:36px;padding-left:18px}
  .stat-bar{left:59px;width:489px;color:#fff;font-weight:600;font-size:15px;padding-left:18px;display:flex;align-items:center}
  .stat-bar--red{background:var(--red);height:48px;top:359px}
  .stat-bar--maroon{background:var(--maroon);height:52px;top:480px}
  .risk-title{left:59px;top:552px;font-size:24px;line-height:1.3;font-weight:500;text-transform:uppercase;color:#333}
  .risk-box{left:59px;top:637px;width:489px;height:164px;border:3px solid var(--maroon);border-right:none;padding:6px 0 0 14px}
  .risk-row{display:flex;align-items:center;height:50px;gap:26px}
  .risk-row+.risk-row .risk-label{border-top:1px solid #cfcfcf}
  .risk-icon{width:50px;height:48px;background:var(--pink);display:flex;align-items:center;justify-content:center}
  .risk-label{flex:1;height:50px;display:flex;align-items:center;font-size:18px;font-weight:500;margin-right:30px}
  .portrait{left:548px;top:159px;width:519px;height:694px;
    background:linear-gradient(170deg,#f3f1ef 0%,#ddd3cc 35%,#9a8c88 62%,#3b4766 100%)}

  .section-head{background:var(--red);color:#fff;font-weight:700;text-transform:uppercase;text-align:center;border-radius:28px 28px 0 0}
  .section-body{background:var(--pink);border-radius:0 0 28px 28px}
  .protect-head{left:59px;width:1021px;top:853px;height:61px;font-size:26px;line-height:61px}
  .protect-body{left:59px;width:1021px;top:914px;height:339px;padding:22px 0 0 36px}
  .checks{list-style:none;color:var(--brown);font-weight:500;font-size:15.5px;line-height:1.3}
  .checks li{position:relative;padding-left:34px;margin-bottom:8px}
  .checks li::before{content:"";position:absolute;left:0;top:4px;width:14px;height:14px;border-radius:50%;background:var(--teal)}
  .checks li::after{content:"";position:absolute;left:4px;top:7px;width:6px;height:3px;border-left:2px solid #fff;border-bottom:2px solid #fff;transform:rotate(-45deg)}
  .checks .sub{list-style:none;margin-top:2px}
  .checks .sub li{padding-left:12px;margin-bottom:3px}
  .checks .sub li::before{content:"•";width:auto;height:auto;background:none;top:0;left:0;border-radius:0}
  .checks .sub li::after{display:none}
  .note{left:128px;top:1278px;width:882px;height:37px;border:1.5px solid #888;text-align:center;font-size:15.5px;line-height:34px;color:var(--brown);font-weight:500}
  .foot-brand{left:149px;top:1353px;width:422px;height:62px;border:2px solid var(--maroon);display:flex;align-items:center;justify-content:center;gap:12px;font-weight:600;font-size:18px;color:var(--maroon)}
  .brand-mark{width:18px;height:18px;background:currentColor}
  .foot-url{left:571px;top:1353px;width:426px;height:62px;background:var(--teal);color:#fff;font-weight:600;font-size:18px;white-space:nowrap;display:flex;align-items:center;justify-content:center}

  /* page two */
  .banner--full{left:0;right:0;top:57px;height:92px;padding:10px 0 0 59px}
  .lead{left:59px;top:168px;width:1020px;font-size:15.5px;line-height:1.3}
  .lead p+p{margin-top:22px}
  .doctor-head{left:59px;width:1021px;top:312px;height:55px;font-size:26px;line-height:58px}
  .doctor-body{left:59px;width:1021px;top:367px;height:478px;padding:20px 60px 0 36px}
  .doctor-body .checks{font-size:15px;line-height:1.28}
  .doctor-body .checks>li{margin-bottom:6px}
  .steps-frame{left:59px;top:984px;width:1021px;height:315px;border:3px solid var(--maroon);padding:48px 60px 0 36px}
  .steps-pill{left:306px;top:955px;width:502px;height:58px;background:var(--red);border:3px solid var(--deep);border-radius:29px;color:#fff;font-weight:700;font-size:26px;line-height:52px;text-align:center;text-transform:uppercase}
  .steps-frame .checks li{margin-bottom:6px}
  .foot-band{left:0;right:0;top:1353px;height:86px;background:var(--pink)}
  .foot-brand--teal{left:417px;top:1350px;width:306px;height:65px;background:var(--teal);color:#fff;display:flex;align-items:center;justify-content:center;gap:12px;font-weight:600;font-size:18px}
</style>
</head>
<body>

<section class="page page--one">
  <h1 class="abs title">Steady Steps,<span class="accent">Bright Days…</span></h1>
  <div class="abs banner banner--side">Keep your heart and body<br>healthy to protect your brain</div>
  <p class="abs intro">Everyone slows down as they get older, both in body and mind. Big changes in memory or thinking that make it hard to get through the day are not a normal part of aging. These changes could be signs of early dementia or Alzheimer’s disease.</p>

  <div class="abs stat-pill" style="top:307px">1 IN 9</div>
  <div class="abs stat-bar stat-bar--red">People in the U.S. ages 65+ has Alzheimer’s dementia</div>
  <div class="abs stat-pill" style="top:429px">1 IN 3</div>
  <div class="abs stat-bar stat-bar--maroon">American Indian people ages 65+ develops dementia</div>

  <h2 class="abs risk-title">You are more at risk of<br>developing dementia if you have</h2>
  <div class="abs risk-box">
    <div class="risk-row">
      <span class="risk-icon"><svg width="26" height="24" viewBox="0 0 26 24"><path d="M13 22 3 12a5.5 5.5 0 0 1 10-7 5.5 5.5 0 0 1 10 7z" fill="var(--teal)"/></svg></span>
      <span class="risk-label">HIGH BLOOD PRESSURE</span>
    </div>
    <div class="risk-row">
      <span class="risk-icon"><svg width="22" height="26" viewBox="0 0 22 26"><rect x="3" y="8" width="16" height="16" rx="3" fill="var(--teal)"/><rect x="8" y="2" width="6" height="7" fill="var(--teal)"/></svg></span>
      <span class="risk-label">DIABETES OR</span>
    </div>
    <div class="risk-row">
      <span class="risk-icon"><svg width="28" height="20" viewBox="0 0 28 20"><rect x="2" y="9" width="22" height="5" rx="1" transform="rotate(-25 13 11)" fill="var(--teal)"/></svg></span>
      <span class="risk-label">YOU SMOKE CIGARETTES</span>
    </div>
  </div>

  <div class="abs portrait" role="img" aria-label="Photo of a smiling older woman in a patterned head scarf and shawl, looking toward the text"></div>

  <div class="abs section-head protect-head">You can protect your body, heart, and mind</div>
  <div class="abs section-body protect-body">
    <ul class="checks">
      <li>Schedule a “wellness” visit and health screenings every year with your doctor, even if you feel ok</li>
      <li>Keep a healthy blood pressure</li>
      <li>Be active or walk every day</li>
      <li>Maintain a healthy weight for your body size</li>
      <li>Eat a healthier diet with more fresh vegetables, fruits, whole grains, and fish</li>
      <li>Stop smoking cigarettes or chewing tobacco</li>
      <li>Get help managing your high blood pressure, diabetes, or to lose extra weight</li>
      <li>Talk to your doctor about how you feel because your mental health can affect your brain &amp; physical health</li>
      <li>If it is hard for you to get through the day because of forgetfulness or memory problems,<br>see your doctor right away</li>
    </ul>
  </div>

  <div class="abs note">You can do these things today to protect your mind and reduce the risk of or slow down dementia.</div>
  <div class="abs foot-brand"><span class="brand-mark"></span>Novel Marrow</div>
  <div class="abs foot-url">https://novelmarrow.org/wellness-path</div>
</section>

<section class="page page--two">
  <div class="abs banner banner--full">The river of life flows through your heart to protect<br>your mind and body</div>
  <div class="abs lead">
    <p>Your heart health plays a big part in the health of your brain. Your heart is like the start of a flowing river. Blood vessels that take blood to and from your heart are like connected streams that flow through your body. They feed your brain with oxygen and energy.</p>
    <p>You can do things to keep the streams freely flowing through your body, so your heart and brain stay strong &amp; healthy.</p>
  </div>

  <div class="abs section-head doctor-head">Working with your doctor</div>
  <div class="abs section-body doctor-body">
    <ul class="checks">
      <li>Make an appointment for a “wellness” checkup with your doctor every year
        <ul class="sub">
          <li>You will get tests and screenings to make sure you are healthy</li>
          <li>They are usually free with Senior Care Plan or the Tribal Wellness Service</li>
          <li>If you have concerns about your memory, talk to your doctor</li>
        </ul></li>
      <li>Have your blood pressure checked and know your numbers
        <ul class="sub">
          <li>Your blood pressure should be less than 120/80 mmHg (120 over 80)</li>
          <li>If you do not know how to take your blood pressure, ask your doctor to show you</li>
        </ul></li>
      <li>Have your weight checked regularly and know your number. If you need to lose extra weight, ask your doctor about:
        <ul class="sub">
          <li>The right number of calories for your body</li>
          <li>Ideas for healthier food choices</li>
          <li>Support for losing weight</li>
        </ul></li>
      <li>If you smoke cigarettes or chew tobacco, ask about medicine, counseling, or help to stop<br>If you do not have diabetes, have your blood sugar level checked during your visit. Your blood sugar should be less than 100 mg/dL when you have not eaten.</li>
      <li>If you do have diabetes, go to regular doctor visits. Have your blood sugar and “A1C” levels checked. Your doctor will tell you what your A1C level should be.</li>
      <li>Talk with your doctor about all the medicines and vitamins you take. Your doctor can make sure they do not cause any problems with your memory, sleep, or brain function.</li>
    </ul>
  </div>

  <div class="abs steps-frame">
    <ul class="checks">
      <li>Aim for 20 minutes of physical activity a day or 2 1/2 hours a week</li>
      <li>Eat less salt, sugar, red meat, and highly processed or packaged foods</li>
      <li>Read food labels to see how much salt (sodium) or fat is in your food</li>
      <li>Manage extra weight by making small changes. Losing a few pounds makes a difference</li>
      <li>Limit alcohol. No more than 1 drink per day for women and 2 for men</li>
      <li>Take your medicine for blood pressure, diabetes, and other problems even if you feel good</li>
      <li>Get at least seven hours of sleep each night. Talk to your doctor if you have trouble sleeping</li>
      <li>Keep your mind active. Visit with people in your community, help plan tribal events, go to your senior center, teach your language, play cards, or start a new hobby.</li>
    </ul>
  </div>
  <div class="abs steps-pill">Other steps you can take</div>

  <div class="abs foot-band"></div>
  <div class="abs foot-brand--teal"><span class="brand-mark"></span>Novel Marrow</div>
</section>

</body>
</html>
```